New business cards for our company KTRV

We need a new business card design for our existing company. We are a consulting/engineering firm which mainly works in the utility business. We would like to see designs which are pretty traditional and simple, with our logo, maybe with an option of a QR code on the back. We plan on using traditional rectangular horizontal format. Want our logo to be in red as attached, then company info in black or blue. I think we want a clean white card, no full color cards. Website is www.ktrv-example.com.

Industry/Entity Type

Business

Contact Information for Business Card

Want a rectangular horizontal business card layout. Probably want a traditional layout with company logo on top right or top left, but open to new ideas. Will want to show company name, address, web address, phone, employee name and title.

Colors
ec1f27
0355a3
ffffff

Requirements
Must have
• business card design,
Nice to have
• QR code on back,
Should not have
• solid back ground card, want white back ground

```html
<!DOCTYPE html>
<html lang="en">
<head>
<meta charset="utf-8">
<title>KTRV Business Card</title>
<link rel="stylesheet" href="https://fonts.googleapis.com/css2?family=Open+Sans:wght@400;600;700;800&display=swap">
<style>
  :root {
    --brand-red: #ec1f27;
    --brand-blue: #0355a3;
    --card-white: #ffffff;
    --ink: #2a2a2a;
    --page: #ecebe8;
  }
  * { box-sizing: border-box; margin: 0; padding: 0; }
  html, body { width: 1200px; height: 780px; overflow: hidden; }
  body {
    background: var(--page);
    font-family: "Open Sans", Arial, sans-serif;
    position: relative;
  }
  .card {
    position: absolute;
    top: 235px;
    width: 540px;
    height: 310px;
    background: var(--card-white);
    box-shadow: 0 2px 10px rgba(0,0,0,0.15);
    overflow: hidden;
  }
  .card--front { left: 50px; }
  .card--back { left: 610px; }
  .card__art { position: absolute; inset: 0; width: 100%; height: 100%; }

  /* Front */
  .brand-name {
    position: absolute; left: 42px; top: 68px;
    font-size: 58px; font-weight: 800; color: var(--brand-red);
    letter-spacing: 1px; line-height: 1;
  }
  .person { position: absolute; left: 44px; top: 144px; }
  .person__name { font-size: 17px; font-weight: 700; color: var(--brand-red); }
  .person__title { font-size: 13px; color: var(--ink); }
  .contact-list { position: absolute; left: 44px; top: 198px; list-style: none; }
  .contact-list li {
    display: flex; align-items: center; gap: 8px;
    font-size: 13px; color: var(--ink); line-height: 19px;
  }
  .contact-list .icon {
    width: 14px; height: 14px; background: var(--brand-red);
    display: inline-flex; align-items: center; justify-content: center;
  }
  .office { position: absolute; right: 34px; top: 170px; text-align: right; }
  .office__web { font-size: 13px; color: var(--brand-red); margin-bottom: 4px; }
  .office__address { font-size: 13px; color: var(--ink); line-height: 18px; }

  /* Back */
  .company { position: absolute; left: 0; right: 0; top: 72px; text-align: center; }
  .company__line {
    font-size: 28px; font-weight: 700; color: var(--brand-red);
    letter-spacing: 1px; line-height: 36px;
  }
  .company__tagline { font-size: 15px; color: var(--brand-blue); margin-top: 6px; }
  .back-band {
    position: absolute; left: 0; right: 0; bottom: 0; height: 58px;
    background: var(--brand-blue); border-top: 5px solid var(--brand-red);
    color: var(--card-white); font-size: 14px;
    display: flex; align-items: center; justify-content: center;
    letter-spacing: 0.3px;
  }
</style>
</head>
<body>
  <section class="card card--front" aria-label="Business card front">
    <svg class="card__art" viewBox="0 0 540 310" aria-hidden="true">
      <path d="M300 0 Q480 30 540 150 L540 0 Z" fill="var(--brand-blue)"/>
      <path d="M0 70 Q250 -30 520 160" fill="none" stroke="var(--brand-red)" stroke-width="2.5"/>
    </svg>
    <div class="brand-name">KTRV</div>
    <div class="person">
      <div class="person__name">Daniel Morrow, P.E.</div>
      <div class="person__title">Project Engineer</div>
    </div>
    <ul class="contact-list">
      <li><span class="icon"><svg width="10" height="10" viewBox="0 0 10 10"><path d="M2 1 L4 1 L4.6 3 L3.5 3.8 Q4.5 6 6.2 6.6 L7 5.5 L9 6 L9 8 Q5 9 2.5 6 Q1 3.5 2 1Z" fill="#fff"/></svg></span>555-210-4400</li>
      <li><span class="icon"><svg width="10" height="10" viewBox="0 0 10 10"><rect x="1" y="4" width="8" height="5" fill="#fff"/><rect x="2.5" y="1" width="5" height="3" fill="none" stroke="#fff"/></svg></span>555-210-4411</li>
      <li><span class="icon"><svg width="10" height="10" viewBox="0 0 10 10"><rect x="3" y="0.5" width="4" height="9" rx="0.8" fill="none" stroke="#fff"/><rect x="4.5" y="7.5" width="1" height="1" fill="#fff"/></svg></span>555-318-7720</li>
      <li><span class="icon"><svg width="10" height="10" viewBox="0 0 10 10"><rect x="1" y="2.5" width="8" height="5.5" fill="none" stroke="#fff"/><path d="M1 2.5 L5 6 L9 2.5" fill="none" stroke="#fff"/></svg></span>dmorrow@ktrv-example.com</li>
    </ul>
    <div class="office">
      <div class="office__web">www.ktrv-example.com</div>
      <div class="office__address">418 Ridgeline Ave<br>Maple Hill, MO 63099</div>
    </div>
  </section>

  <section class="card card--back" aria-label="Business card back">
    <div class="company">
      <div class="company__line">KTRV ENGINEERS</div>
      <div class="company__line">KTRV SERVICE CORP.</div>
      <div class="company__tagline">Engineers Serving Utilities</div>
    </div>
    <div class="back-band">418 Ridgeline Ave, Maple Hill, MO 63099</div>
  </section>
</body>
</html>
```